Dental Website offering Continuing Educational Courses

Need a Wordpress CMS design for a dentist website which will offer continuing education courses. The design should be professional, simple and elegant. Logo versions are provided. Please follow those colors plus one or two others that will blend well. Here's examples of other sites they like - www.pelvaronix.com, www.qortiva.com, www.thebriselmoreinstitute.com., www.kwjt.org/. Please provide designs in jpg format. If selected, then final design will be required in psd format.

Target Market(s)

dentists, endodontists (root canal specialists)

Industry/Entity Type

Education

Requirements
Must have
• Combination Horizontal / Vertical navigation. Place course titles in vertical nav in a side bar on home page. List them as Course 1, Course 2 ,etc.. total of 7 courses. The header horizontal nav should be; Home, About, Courses, Doctor Name, Faculty, FAQ, Patients, Contact.
Need placeholder to accommodate one large static image just under main nav. Need web safe fonts. Need placeholder for calendar like this example www.tumbledfields.org/. Need to show a dropdown menu example. Design for 1024 x 768. Need space on home page to allow for logos of external websites/ associations. These are; www.fennicoralbo.com, www.yarplova.com, www.hmu.org/, www.corvintagha.com/corv/. Would like to see a row of images across the bottom of the home page like the www.kwjt.org site has. Would like to show a Contact Form on the home page like the "need assistance" form example on www.thebriselmoreinstitute.com. Would like to create a placeholder on the home page for an image of a doctor.
Nice to have
• 3 or 4 column footer (which features sitemap, copyright, etc..). Examples in the design for the web site’s copy styling:
o through headers
o Bulleted list
o Hyperlink
o Table

```html
<!DOCTYPE html>
<html lang="en">
<head>
<meta charset="utf-8">
<title>Yarplova Teaching – Continuing Dental Education</title>
<link href="https://fonts.googleapis.com/css2?family=Open+Sans:wght@400;600;700&family=Roboto+Condensed:wght@400;700&family=Tinos:ital,wght@0,400;0,700;1,400&display=swap" rel="stylesheet">
<style>
:root{
  --page-bg:#e8eef3;
  --navy:#0b2d57;
  --navy-deep:#062c5a;
  --blue:#0a5cb5;
  --blue-bright:#0b66cc;
  --blue-title:#0d4f9c;
  --white:#ffffff;
  --text:#8a8f96;
  --text-dark:#444;
  --line:#d6dde4;
  --green:#6f9a2c;
  --cal-dark:#2b2f35;
}
*{box-sizing:border-box;margin:0;padding:0}
html,body{width:1050px;height:1200px;overflow:hidden}
body{background:var(--page-bg);font-family:"Open Sans",Arial,sans-serif;position:relative}
.footer-band{position:absolute;left:0;top:963px;width:1050px;height:237px;background:var(--navy-deep)}
.page{position:absolute;left:151px;top:0;width:750px;height:1200px;background:var(--white)}
.page-foot{position:absolute;left:151px;top:963px;width:750px;height:237px;background:var(--blue-bright)}
.topline{position:absolute;left:0;top:0;width:1050px;height:6px;background:#555}
.main-nav{position:absolute;left:151px;top:6px;width:750px;height:31px;background:var(--navy);display:flex;align-items:center;justify-content:space-around;padding:0 20px}
.main-nav a{color:var(--white);font:700 12px "Open Sans",Arial,sans-serif;text-decoration:none;letter-spacing:.2px}
.dropdown{position:absolute;left:339px;top:37px;width:101px;height:98px;background:var(--blue-bright);padding:5px 3px;z-index:3}
.dropdown a{display:block;color:var(--white);font:700 10.5px "Open Sans",Arial,sans-serif;padding:2px 19px;height:18px;text-decoration:none}
.dropdown a.active{background:#e6eef8;color:var(--blue)}
.header{position:absolute;left:161px;top:46px;width:730px;height:89px;background:var(--blue);display:flex;align-items:center;justify-content:space-between;padding:0 12px}
.brand{display:flex;align-items:center;gap:8px;color:var(--white);font:700 21px/23px "Open Sans",Arial,sans-serif}
.brand-mark{width:18px;height:18px;background:var(--white);flex:none}
.call{color:var(--white);font-family:"Tinos",serif;text-align:right}
.call small{display:block;font-size:13px;text-transform:uppercase}
.call strong{font-weight:400;font-size:30px;letter-spacing:.5px}
.hero{position:absolute;left:162px;top:145px;width:522px;height:218px;background:linear-gradient(90deg,#d7b39a,#c98e62 40%,#9b6a4a 70%,#d3a57d)}
.welcome{position:absolute;left:162px;top:378px;width:522px}
.welcome h1{font:400 21px/28px "Roboto Condensed",Arial,sans-serif;color:var(--blue-title);margin-bottom:2px}
.welcome p{font-size:9.4px;line-height:13.5px;color:var(--text)}
.welcome .intro{width:320px;margin-bottom:8px}
.doctor-photo{position:absolute;left:494px;top:394px;width:166px;height:113px;border:4px solid var(--white);box-shadow:0 2px 5px rgba(0,0,0,.3);background:linear-gradient(90deg,#6d4b3a,#c9b7a5 55%,#e6dbd0)}
.read-more{position:absolute;left:576px;top:621px;width:72px;height:22px;background:#f1f3f5;border:1px solid var(--line);border-radius:3px;font:700 10px "Tinos",serif;color:var(--blue-title);display:flex;align-items:center;justify-content:center;gap:6px}
.divider{position:absolute;left:220px;top:651px;width:370px;height:2px;background:linear-gradient(90deg,transparent,#cfd5db,transparent)}
.card{position:absolute;top:664px;height:150px;border:1px solid var(--line);background:var(--white)}
.card-head{height:26px;border-bottom:1px solid var(--line);display:flex;justify-content:space-between;align-items:center;padding:0 10px;background:linear-gradient(#fff,#f0f3f6)}
.card-head h2{font:700 15px "Tinos",serif;color:var(--blue-title)}
.card-head span{font:700 11px Arial,sans-serif;color:var(--blue-title)}
.testimonials{left:171px;width:210px}
.quote{padding:14px 12px 10px;font:italic 11.5px/17px "Tinos",serif;color:var(--text-dark)}
.quote-by{text-align:right;padding-right:30px;font:italic 700 9px Arial,sans-serif;color:#555;line-height:11px}
.upcoming{left:419px;width:244px}
.course-photo{position:absolute;left:8px;top:36px;width:112px;height:94px;background:linear-gradient(135deg,#6f8fa7,#d9c1ae 55%,#f0e4da)}
.course-info{position:absolute;left:132px;top:34px;width:104px;font-size:9px;color:var(--text);line-height:13px}
.course-info b{color:#777}
.course-info p{margin-top:8px;font-size:8px;line-height:12px}
.sidebar-rule{position:absolute;left:684px;top:363px;width:1px;height:455px;background:#eceff2}
.events{position:absolute;left:692px;top:145px;width:199px;height:411px;background:var(--blue-bright);border:1px solid #0a4f9e}
.events-head{display:flex;justify-content:space-between;align-items:center;padding:4px 8px;color:var(--white)}
.events-head h2{font:400 19px "Roboto Condensed",Arial,sans-serif}
.events-head a{font-size:9px;color:var(--white);text-decoration:none}
.calendar{margin:6px 9px 0;background:#f4f5f6}
.cal-title{background:var(--cal-dark);color:var(--white);font:700 10.5px Arial,sans-serif;display:flex;justify-content:space-between;padding:6px 10px}
.cal-grid{display:grid;grid-template-columns:repeat(7,1fr);gap:1px;background:#d4d8dc;border:1px solid #d4d8dc}
.cal-grid span{background:#fafafa;height:25px;font:9.5px Arial,sans-serif;display:flex;align-items:center;justify-content:center;color:#333}
.cal-grid .dow{height:14px;font-size:7.5px;background:#eceef0;color:#555}
.cal-grid .out{color:#aaa}
.cal-grid .today{background:#3a3f46;color:var(--white)}
.cal-grid .shade{background:#dfe2e5}
.available{margin:8px 4px 0;background:var(--white);color:var(--blue-bright);text-align:center;font:700 12.5px "Open Sans",Arial,sans-serif;padding:2px 0}
.course-list{list-style:none;margin-top:6px}
.course-list li{font-size:7.8px;line-height:12px;color:var(--white);padding:7px 8px 7px 20px;position:relative;height:39px}
.course-list li::before{content:"";position:absolute;left:8px;top:10px;border:3px solid transparent;border-left:4px solid var(--white)}
.course-list li.active{background:#e4edf7;color:var(--blue)}
.course-list li.active::before{border-left-color:var(--blue)}
.assist{position:absolute;left:692px;top:573px;width:199px;height:241px;border:1px solid var(--line)}
.assist h2{font:700 15px "Tinos",serif;color:var(--navy);padding:4px 14px;height:27px;border-bottom:1px solid var(--line);background:linear-gradient(#fff,#f0f3f6)}
.field{display:flex;align-items:center;justify-content:space-between;padding:0 6px 0 10px;height:22px;font-size:9px;color:#555}
.field i{width:134px;height:17px;border:1px solid var(--line);display:block}
.assist form{padding-top:8px}
.msg{margin:2px 6px 0 12px;height:50px;border:1px solid var(--line)}
.submit{position:absolute;right:14px;bottom:16px;width:64px;height:20px;background:var(--green);color:var(--white);font:700 9px "Tinos",serif;display:flex;align-items:center;justify-content:center;border-radius:2px}
.links{position:absolute;left:167px;top:834px;width:719px;height:108px;border:1px solid var(--line);display:flex;align-items:center}
.links-tab{position:absolute;left:1px;top:2px;width:30px;height:100px;background:var(--green);display:flex;align-items:center;justify-content:center}
.links-tab span{transform:rotate(-90deg);color:var(--white);font:400 14px "Tinos",serif;letter-spacing:1.5px}
.partners{display:flex;justify-content:space-around;align-items:center;width:100%;padding-left:40px}
.partner{display:flex;align-items:center;gap:6px;font:700 12px "Tinos",serif;color:#222}
.partner i{width:12px;height:12px;background:#222;display:block}
.partner.dark{background:#222;color:var(--white);padding:6px 8px}
.partner.dark i{background:var(--white)}
.footer-box{position:absolute;left:165px;top:978px;width:721px;height:117px;background:var(--blue);border:1px solid #0a4a94;border-radius:4px;display:grid;grid-template-columns:130px 130px 122px 103px 118px 1fr;padding:14px 0 0 32px}
.footer-box h3{color:var(--white);font:600 10px "Open Sans",Arial,sans-serif;margin-bottom:14px}
.footer-box a,.footer-box p{display:block;color:#bcd3ee;font-size:9px;line-height:15.5px;text-decoration:none}
.social{display:grid;grid-template-columns:22px 22px;gap:14px 14px;margin-left:2px}
.social i{width:22px;height:22px;border-radius:50%;background:#e6ecf3;display:block}
.footer-nav{position:absolute;left:185px;top:1095px;width:688px;height:37px;background:var(--navy-deep);display:flex;justify-content:center;align-items:center;gap:14px;color:#cfe0f4;font-size:9px}
.copyright{position:absolute;left:151px;top:1147px;width:750px;text-align:center;color:#d5e3f4;font-size:8.5px}
</style>
</head>
<body>
<div class="footer-band"></div>
<div class="topline"></div>
<div class="page"></div>
<div class="page-foot"></div>

<nav class="main-nav">
  <a href="#">HOME</a><a href="#">ABOUT</a><a href="#">COURSES</a><a href="#">DOCTOR NAME</a><a href="#">FACULTY</a><a href="#">FAQ</a><a href="#">CONTACT</a>
</nav>
<div class="dropdown">
  <a href="#">Course 1</a><a href="#" class="active">Course 2</a><a href="#">Course 3</a><a href="#">Course 4</a><a href="#">Course 5</a>
</div>

<header class="header">
  <div class="brand"><span class="brand-mark"></span><span>Yarplova<br>Teaching</span></div>
  <div class="call"><small>Call for inquiries!</small><strong>123 456 7890</strong></div>
</header>

<div class="hero" role="img" aria-label="Large banner photo of smiling dental students"></div>

<section class="welcome">
  <h1>WELCOME</h1>
  <p class="intro">Lorem ipsum dolor sit amet, consectetuer adipiscing elit. Aecommodo ligula eget dolor.Lorem ipsum dolor sit amet, consectetuer adip. AenLorem ipsum dolor sitmet, condolor.Loreor sit amet, coLorem ips sit amet, consectetuer adipiscing elit. Aesectetuer adipiscing elit. ean commodligula eget dolor.ean commodo ligulat dolor.Loreor sit amet, coLorem ips sit adolor. Aemet, consectetuer adipiscing elit. Aecommodo ligula eget dolor.</p>
  <p>Lorem ipsum dolor sit amet, consectetuer adipiscing elit. Aeneacommodo ligula eget dolor.Lorem ipsum dolor sit amecon-sectetueradipiscing elit. ean commodo ligula eget dolor.ean commodo ligulat dolor.Loreor sit amet, consectetuer adipiscing elit. Aenean commodo liguleglLoremet, consectetuer adipiscing elit. Aenean commodo ligula eget doLorem ipsnsectetuer adipiscing elit. Aenean commodo liguleglLoremet, consectetuer adipiscing elit. AenLorem ips dolor sitmet, consectetuer adipiscing elit. ean commodo ligula eget dolor.ean commodo ligulat dolAenLorem ips dolor sitmet, consectetuer adipiscing elit. ean commodo ligula eget dolor.</p>
</section>
<div class="doctor-photo" role="img" aria-label="Photo of a doctor examining a young patient"></div>
<div class="read-more">Read more
  <svg width="7" height="9" viewBox="0 0 7 9"><path d="M1 1l4 3.5L1 8" stroke="#0d4f9c" stroke-width="2" fill="none"/></svg>
</div>
<div class="divider"></div>

<section class="card testimonials">
  <div class="card-head"><h2>Testimonials</h2><span>‹ ›</span></div>
  <p class="quote">Lorem ipsum dolor siamet, consectetuer g elit. Aenean commodo ligula eget Aenean masula eget dolor. Aenean massa. Cum sociis natoque”</p>
  <p class="quote-by">- &nbsp;MAREN<br>student</p>
</section>

<section class="card upcoming">
  <div class="card-head"><h2>Upcoming Courses</h2><span>‹ ›</span></div>
  <div class="course-photo" role="img" aria-label="Photo of a patient at a dental check-up"></div>
  <div class="course-info">
    Name of the Courses<br><b>Date : 31/01/2012</b><br><b>Time : 9:00 Am</b>
    <p>Lorem ipsum dolor sit amet, consectetuer adipiscing elit. Aenean commodo ligula eget dolor.</p>
  </div>
</section>

<div class="sidebar-rule"></div>

<aside class="events">
  <div class="events-head"><h2>EVENTS</h2><a href="#">View all Events</a></div>
  <div class="calendar">
    <div class="cal-title"><span>◄</span><span>April 2011</span><span>►</span></div>
    <div class="cal-grid">
      <span class="dow">MON</span><span class="dow">TUE</span><span class="dow">WED</span><span class="dow">THU</span><span class="dow">FRI</span><span class="dow">SAT</span><span class="dow">SUN</span>
      <span class="out">28</span><span class="out">29</span><span class="out">30</span><span class="out">31</span><span>1</span><span>2</span><span>3</span>
      <span class="today">4</span><span>5</span><span class="shade">6</span><span>7</span><span>8</span><span>9</span><span>10</span>
      <span>11</span><span>12</span><span>13</span><span>14</span><span>15</span><span>16</span><span>17</span>
      <span>18</span><span>19</span><span>20</span><span>21</span><span>22</span><span>23</span><span>24</span>
      <span>25</span><span>26</span><span>27</span><span>28</span><span>29</span><span>30</span><span class="out">1</span>
    </div>
  </div>
  <div class="available">Current Available Courses</div>
  <ul class="course-list">
    <li>Lorem ipsum dolor sit amet, consectetuer adipiscing elit. Aenean commodo.</li>
    <li class="active">Lorem ipsum dolor sit amet, consectetuer adipiscing elit. Aenean commodo.</li>
    <li>Lorem ipsum dolor sit amet, consectetuer adipiscing elit. Aenean commodo.</li>
    <li>Lorem ipsum dolor sit amet, consectetuer adipiscing elit. Aenean commodo.</li>
  </ul>
</aside>

<aside class="assist">
  <h2>Need Assistance?</h2>
  <form>
    <div class="field">Name<i></i></div>
    <div class="field">email ID<i></i></div>
    <div class="field">phone no<i></i></div>
    <div class="field">Address<i></i></div>
    <div class="field">Messagebox</div>
    <div class="msg"></div>
  </form>
  <div class="submit">Submit</div>
</aside>

<section class="links">
  <div class="links-tab"><span>LINKS</span></div>
  <div class="partners">
    <div class="partner"><i></i>Hmu Academy</div>
    <div class="partner"><i></i>Corvintagha Endo</div>
    <div class="partner dark"><i></i>The Briselmore Institute</div>
    <div class="partner"><i></i>Hmu Academy</div>
  </div>
</section>

<footer>
  <div class="footer-box">
    <div><h3>Company</h3><a href="#">About us</a><a href="#">Vision</a><a href="#">Team</a><a href="#">Success Stories</a></div>
    <div><h3>Student</h3><a href="#">Tests</a><a href="#">Educational Loans</a><a href="#">Faqs</a></div>
    <div><h3>Why us</h3><a href="#">Why Choose Us</a><a href="#">Testimonials</a><a href="#">Press Clips</a><a href="#">Photo Gallery</a></div>
    <div><h3>Online</h3><a href="#">Enquiry</a><a href="#">Registration</a><a href="#">Feedback</a></div>
    <div><h3>Contacts</h3><p>Lorem ipsum dolor sit amet, consectetuer adipiscing elit. Aenean commodo</p></div>
    <div><h3>Follow Us</h3><div class="social"><i></i><i></i><i></i><i></i></div></div>
  </div>
  <div class="footer-nav">
    <span>Home</span>|<span>About</span>|<span>Courses</span>|<span>Doctor Name</span>|<span>Faculty</span>|<span>FAQ</span>|<span>Patients</span>|<span>Contact</span>
  </div>
  <p class="copyright">Copyright © 2012</p>
</footer>
</body>
</html>
```